Create a bold and border around my logo to make it pop and sign graphic design

I would like someone to create a sign graphic design so I can use on the side of my trucks and put on yard signs. I would to remove a lot of the white and add more of the orange and blue to give it more pop when cars drive past. I would like the services to be removed and for you to leave space for a mobile number that i would add later. I don’t want my logo changed at all. I just want colour and design to be added to the background so i can use it in signage. Same colour as on the sign

```html
<!DOCTYPE html>
<html lang="en">
<head>
<meta charset="utf-8">
<title>Leafworthy Sign</title>
<link rel="stylesheet" href="https://fonts.googleapis.com/css2?family=Questrial&display=swap">
<style>
  :root {
    --navy: #05377a;
    --orange: #f15a2b;
    --white: #ffffff;
  }
  html, body {
    margin: 0;
    padding: 0;
    overflow: hidden;
    background: var(--white);
  }
  .sign {
    position: relative;
    width: 1200px;
    height: 652px;
    background: var(--white);
    overflow: hidden;
  }
  .sign__header {
    position: absolute;
    inset: 0 0 auto 0;
    width: 1200px;
    height: 360px;
  }
  .sign__header .arc-accent { fill: var(--orange); }
  .sign__header .arc-band { fill: var(--navy); }
  .sign__header .brand-dot { fill: var(--white); }
  .brand-name {
    position: absolute;
    top: 360px;
    left: 0;
    width: 1200px;
    margin: 0;
    text-align: center;
    font-family: "Questrial", sans-serif;
    font-weight: 400;
    font-size: 118px;
    line-height: 118px;
    letter-spacing: 4px;
    color: var(--navy);
  }
  .stripe {
    position: absolute;
    left: 0;
    width: 1200px;
  }
  .stripe--orange { top: 609px; height: 17px; background: var(--orange); }
  .stripe--navy { top: 629px; height: 16px; background: var(--navy); }
</style>
</head>
<body>
  <div class="sign">
    <svg class="sign__header" viewBox="0 0 1200 360" aria-hidden="true">
      <path class="arc-accent" d="M0 0 H1200 V238 Q600 452 0 238 Z"/>
      <path class="arc-band" d="M0 0 H1200 V217 Q600 471 0 217 Z"/>
      <circle class="brand-dot" cx="600" cy="210" r="130"/>
    </svg>
    <h1 class="brand-name">LEAFWORTHY</h1>
    <div class="stripe stripe--orange"></div>
    <div class="stripe stripe--navy"></div>
  </div>
</body>
</html>
```